The Timber Loft

We need a business card design for our wardrobe company.
Please visit our website www.zorvelcabinets.com to get an idea of who we are.

```html
<!DOCTYPE html>
<html lang="en">
<head>
<meta charset="utf-8">
<title>The Timber Loft – Business Card</title>
<link rel="stylesheet" href="https://fonts.googleapis.com/css2?family=Lato:wght@400;700&display=swap">
<style>
  :root {
    --backdrop: #4a4a4a;
    --card-light: #f6f6f6;
    --card-shade: #e9e9e9;
    --ink: #3e3e3e;
    --band: #454344;
    --band-text: #f2f2f2;
    --icon-glyph: #f4f4f4;
  }
  * { box-sizing: border-box; margin: 0; padding: 0; }
  html, body {
    width: 1200px;
    height: 818px;
    overflow: hidden;
    background: var(--backdrop);
    font-family: "Lato", Arial, sans-serif;
    color: var(--ink);
  }
  .business-card {
    position: absolute;
    left: 75px;
    top: 109px;
    width: 1050px;
    height: 600px;
    background: linear-gradient(135deg, var(--card-light) 0%, var(--card-shade) 100%);
    overflow: hidden;
  }
  .brand-block {
    position: absolute;
    right: 355px;
    top: 88px;
    text-align: right;
  }
  .brand-name {
    font-size: 34px;
    font-weight: 400;
    letter-spacing: 3px;
    text-transform: uppercase;
    line-height: 1;
    margin-right: -3px;
  }
  .brand-tagline {
    margin-top: 12px;
    font-size: 24px;
    letter-spacing: 5.2px;
    line-height: 1;
    margin-right: -5px;
  }
  .brand-square {
    position: absolute;
    left: 743px;
    top: 71px;
    width: 120px;
    height: 120px;
    background: var(--ink);
  }
  .contact-list {
    position: absolute;
    left: 58px;
    top: 250px;
    list-style: none;
    font-size: 27px;
    letter-spacing: 0.6px;
    line-height: 39px;
  }
  .contact-item {
    display: flex;
    align-items: flex-start;
  }
  .contact-icon {
    width: 30px;
    height: 30px;
    margin-top: 5px;
    margin-right: 20px;
    flex-shrink: 0;
  }
  .contact-address {
    display: block;
    font-style: normal;
  }
  .web-band {
    position: absolute;
    left: 0;
    top: 498px;
    width: 100%;
    height: 48px;
    background: var(--band);
    color: var(--band-text);
    font-size: 35px;
    letter-spacing: 4.5px;
    line-height: 48px;
    text-align: center;
  }
</style>
</head>
<body>
  <main class="business-card">
    <header class="brand-block">
      <h1 class="brand-name">The Timber Loft</h1>
      <p class="brand-tagline">Crafted to Fit Your Home</p>
    </header>
    <div class="brand-square" aria-hidden="true"></div>

    <ul class="contact-list">
      <li class="contact-item">
        <svg class="contact-icon" viewBox="0 0 30 30" aria-hidden="true">
          <circle cx="15" cy="15" r="15" fill="var(--ink)"/>
          <rect x="10" y="6.5" width="10" height="17" rx="2" fill="none" stroke="var(--icon-glyph)" stroke-width="2"/>
          <circle cx="15" cy="20" r="1.2" fill="var(--icon-glyph)"/>
        </svg>
        <span>0207 555 0148</span>
      </li>
      <li class="contact-item">
        <svg class="contact-icon" viewBox="0 0 30 30" aria-hidden="true">
          <circle cx="15" cy="15" r="15" fill="var(--ink)"/>
          <rect x="7.5" y="9.5" width="15" height="11" rx="1" fill="none" stroke="var(--icon-glyph)" stroke-width="1.8"/>
          <polyline points="7.5,10 15,16 22.5,10" fill="none" stroke="var(--icon-glyph)" stroke-width="1.8"/>
        </svg>
        <span>info@zorvelcabinets.com</span>
      </li>
      <li class="contact-item">
        <svg class="contact-icon" viewBox="0 0 30 30" aria-hidden="true">
          <circle cx="15" cy="15" r="15" fill="var(--ink)"/>
          <path d="M15 6.5a6 6 0 0 0-6 6c0 4.5 6 11 6 11s6-6.5 6-11a6 6 0 0 0-6-6z" fill="var(--icon-glyph)"/>
          <circle cx="15" cy="12.5" r="2.3" fill="var(--ink)"/>
        </svg>
        <address class="contact-address">
          Harlow Court<br>
          48 Fenmore Street<br>
          London EC2A 4PT
        </address>
      </li>
    </ul>

    <footer class="web-band">zorvelcabinets.com</footer>
  </main>
</body>
</html>
```